Maple Ridge business card design

Card needs to include the following text/items:
Company Logo
Tobin Marsh
Phone # - 555-318-7642
service@mapleridgelandscaping.example
Lawn & landscape maintenance services

```html
<!DOCTYPE html>
<html lang="en">
<head>
<meta charset="utf-8">
<title>Maple Ridge Landscaping – Business Card</title>
<link href="https://fonts.googleapis.com/css2?family=Arimo:wght@400;700&display=swap" rel="stylesheet">
<style>
  :root {
    --stage: #18212b;
    --sky: #33bbf0;
    --sky-light: #bfe8fa;
    --meadow: #7f9a3a;
    --meadow-light: #9db55a;
    --hill: #5b9a6a;
    --forest: #0d4a2a;
    --forest-mid: #2f6e3e;
    --paper: #ffffff;
    --ink-grey: #5f5f5f;
    --rule: #6d6d6d;
  }
  * { margin: 0; padding: 0; box-sizing: border-box; }
  html, body { width: 1200px; height: 900px; overflow: hidden; }
  body { background: var(--stage); position: relative; font-family: "Arimo", Arial, sans-serif; }

  .card {
    position: absolute;
    left: 250px;
    width: 700px;
    height: 400px;
    overflow: hidden;
    box-shadow: 0 12px 30px rgba(0,0,0,0.45);
  }
  .card--back { top: 35px; }
  .card--front { top: 465px; background: var(--paper); }

  /* Reverse side */
  .back-scene {
    position: absolute; inset: 0;
    background: linear-gradient(180deg, var(--sky) 0%, #49b4d2 28%, var(--hill) 52%, var(--meadow) 78%, var(--meadow-light) 100%);
  }
  .back-name {
    position: absolute;
    left: 0; right: 0; top: 160px;
    text-align: center;
    color: var(--paper);
    font-weight: 700;
    font-size: 50px;
    line-height: 1.1;
  }

  /* Front side */
  .front-art { position: absolute; inset: 0; width: 700px; height: 400px; }

  .brand {
    position: absolute;
    left: 40px; top: 200px;
    display: flex;
    align-items: center;
    gap: 14px;
  }
  .brand__dot {
    width: 44px; height: 44px;
    border-radius: 50%;
    background: var(--forest);
    flex: none;
  }
  .brand__name {
    color: var(--forest);
    font-weight: 700;
    font-size: 26px;
    line-height: 1.15;
  }

  .contact-name {
    position: absolute;
    right: 48px; top: 200px;
    color: var(--forest);
    font-weight: 700;
    font-size: 28px;
    letter-spacing: 0.03em;
  }
  .contact-list {
    position: absolute;
    right: 42px; top: 262px;
    list-style: none;
    color: var(--ink-grey);
    font-size: 17px;
    text-align: right;
  }
  .contact-list li { display: flex; align-items: center; justify-content: flex-end; gap: 10px; height: 26px; }
  .contact-icon { width: 18px; height: 18px; flex: none; }

  .divider {
    position: absolute;
    left: 40px; right: 40px; top: 350px;
    border-top: 1.5px solid var(--rule);
  }
  .tagline {
    position: absolute;
    left: 0; right: 0; top: 360px;
    text-align: center;
    color: var(--ink-grey);
    font-size: 18px;
    letter-spacing: 0.02em;
  }
</style>
</head>
<body>

  <section class="card card--back" aria-label="Business card, reverse side">
    <div class="back-scene" role="img" aria-label="Soft faded countryside scene with trees, hills, a fence and a path"></div>
    <div class="back-name">Maple Ridge<br>Landscaping</div>
  </section>

  <section class="card card--front" aria-label="Business card, front side">
    <svg class="front-art" viewBox="0 0 700 400" aria-hidden="true">
      <defs>
        <linearGradient id="sceneFade" x1="0" y1="0" x2="0.35" y2="1">
          <stop offset="0" stop-color="var(--sky)"/>
          <stop offset="0.35" stop-color="var(--sky-light)"/>
          <stop offset="0.7" stop-color="var(--forest-mid)"/>
          <stop offset="1" stop-color="var(--meadow)"/>
        </linearGradient>
      </defs>
      <rect class="front-scene" role="img" aria-label="Countryside scene with trees, a sun, hills and a white fence"
            x="0" y="0" width="700" height="230" fill="url(#sceneFade)"/>
      <path class="front-band" d="M0,158 C110,72 260,78 390,136 C520,194 625,180 655,0 L700,0 L700,400 L0,400 Z" fill="var(--forest)"/>
      <path class="front-body" d="M0,178 C110,92 260,96 390,152 C520,208 640,196 672,0 L700,0 L700,400 L0,400 Z" fill="var(--paper)"/>
    </svg>

    <div class="brand">
      <span class="brand__dot" aria-hidden="true"></span>
      <span class="brand__name">Maple Ridge<br>Landscaping</span>
    </div>

    <div class="contact-name">TOBIN MARSH</div>
    <ul class="contact-list">
      <li>
        <span>555-318-7642</span>
        <svg class="contact-icon" viewBox="0 0 20 20" aria-hidden="true">
          <circle cx="10" cy="10" r="10" fill="var(--forest)"/>
          <path d="M6.5,5 L8.5,5 L9.3,7.6 L8.1,8.6 C8.7,10 9.9,11.2 11.4,11.9 L12.4,10.7 L15,11.5 L15,13.5 C15,14.2 14.4,14.8 13.7,14.7 C9.5,14.3 5.7,10.5 5.3,6.3 C5.2,5.6 5.8,5 6.5,5 Z" fill="var(--paper)"/>
        </svg>
      </li>
      <li>
        <span>service@mapleridgelandscaping.example</span>
        <svg class="contact-icon" viewBox="0 0 20 20" aria-hidden="true">
          <circle cx="10" cy="10" r="10" fill="var(--forest)"/>
          <rect x="5" y="6.5" width="10" height="7" fill="none" stroke="var(--paper)" stroke-width="1.4"/>
          <path d="M5,6.5 L10,10.8 L15,6.5" fill="none" stroke="var(--paper)" stroke-width="1.4"/>
        </svg>
      </li>
    </ul>

    <div class="divider"></div>
    <p class="tagline">Lawn &amp; Landscape Maintenance Services</p>
  </section>

</body>
</html>
```